Redesign for Popular UK Town Website

We're looking for someone to redesign a website for a popular tourist town that's visited by over 250,000 people a year. We have a basic design frame in place and need someone to make it look more 'professional.'
We've created a temporary design layout to show you a general idea of what we're looking for: http://dorrin.co.uk/
All text/images are placeholder images so you can get an idea of the general layout.
(Please note that you can grab any images found on the internet for 'tenby' to be used as placeholder images. This is because we will be visiting the locations and taking our own photos, after the design is complete.)
Target Market(s)
Tourists
Industry/Entity Type
Town
Number of Pages Required
2 page
Requirements
Must have
- You need to redesign the homepage: http://dorrin.co.uk/
- You also need to redesign the following page: http://dorrin.co.uk/hotels/ (This page will be used for multiple categories and is used to list locations of properties/places etc.)
- Design must be responsive also.
Nice to have
- Please feel free to add as much as you can to the content/features as with our limited knowledge of websites, have only been able to create a basic layout.

```html
<!DOCTYPE html>
<html lang="en">
<head>
<meta charset="utf-8">
<title>Harbourlight – Hotels in Tenby</title>
<link rel="stylesheet" href="https://fonts.googleapis.com/css2?family=Squada+One&family=Arimo:ital,wght@0,400;0,700;1,400&display=swap">
<style>
:root{
  --brown:#8a4b1b;
  --brown-dark:#6f3a12;
  --navy:#1d4e6e;
  --card-blue:#245a80;
  --text:#555;
  --header-bg:#e9e9e9;
  --white:#fff;
}
*{box-sizing:border-box;margin:0;padding:0}
html,body{width:1200px;height:2439px;overflow:hidden;background:var(--white)}
body{position:relative;font-family:"Arimo",Arial,sans-serif;color:var(--text)}
.display{font-family:"Squada One","Arial Narrow",sans-serif}

.site-header{position:absolute;left:0;top:0;width:1200px;height:115px;background:var(--header-bg)}
.brand{position:absolute;left:76px;top:18px;display:flex;align-items:center;gap:12px}
.brand-mark{width:62px;height:62px;border-radius:50%;background:var(--navy)}
.brand-name{font-family:"Squada One",sans-serif;font-size:40px;color:var(--navy)}
.login{position:absolute;right:82px;top:16px;font-size:16px;color:#666;display:flex;align-items:center;gap:8px}
.phone{position:absolute;left:596px;top:56px;display:flex;align-items:center;gap:12px;font-family:"Squada One",sans-serif;font-size:30px;color:#333}
.search{position:absolute;left:790px;top:52px;width:330px;height:44px;border-radius:22px;background:var(--white);border:1px solid #ddd;font-size:14px;color:#666;padding:14px 18px}
.search-btn{position:absolute;right:3px;top:3px;width:36px;height:36px;border-radius:50%;background:var(--brown);display:flex;align-items:center;justify-content:center}

.main-nav{position:absolute;left:0;top:115px;width:1200px;height:62px;background:var(--white)}
.main-nav a{position:absolute;top:0;height:62px;line-height:62px;font-size:17px;color:#333;text-decoration:none;text-transform:uppercase;letter-spacing:.3px}
.main-nav a.active{background:var(--brown);color:var(--white);padding:0 16px}

.hero{position:absolute;left:0;top:177px;width:1200px;height:500px;background:linear-gradient(100deg,#8b7562 0%,#a48c74 35%,#b9a48c 60%,#8d7a5e 100%)}
.hero-title{position:absolute;left:78px;top:130px;font-size:118px;line-height:1;color:var(--white)}
.hero-text{position:absolute;left:78px;top:255px;width:740px;font-size:22px;line-height:1.5;color:var(--white)}
.btn{display:inline-block;background:var(--brown);color:var(--white);font-family:"Squada One",sans-serif;text-transform:uppercase;border-radius:32px;text-align:center;box-shadow:0 3px 6px rgba(0,0,0,.3)}
.hero .btn{position:absolute;left:78px;top:338px;width:188px;height:62px;line-height:62px;font-size:29px}
.slider-arrow{position:absolute;top:228px;width:40px;height:36px;background:var(--navy);display:flex;align-items:center;justify-content:center}

.section-title{position:absolute;left:0;top:738px;width:1200px;display:flex;justify-content:center;align-items:center;gap:14px;font-size:52px;color:var(--navy)}
.section-title .accent{color:var(--brown)}
.title-mark{width:46px;height:46px;border-radius:50%;background:var(--navy)}
.intro{position:absolute;left:150px;top:812px;width:900px;text-align:center;font-size:14.5px;line-height:1.85;color:#666}
.intro strong{color:#444}

.photo{position:absolute}
.hotel-card{position:absolute;left:77px;top:896px;width:334px;height:239px;background:var(--card-blue);color:var(--white);padding-top:36px;text-align:center}
.hotel-card h3{font-family:"Squada One",sans-serif;font-weight:400;font-size:30px;margin-bottom:18px}
.hotel-card .line{display:flex;align-items:center;justify-content:center;gap:10px;margin-bottom:10px}
.hotel-card .tel{font-size:21px}
.hotel-card .small{font-size:15px}

.tagline{position:absolute;left:200px;top:2087px;width:800px;text-align:center;font-style:italic;font-size:18.5px;line-height:1.75;color:var(--navy)}
.more{position:absolute;left:516px;top:2166px;width:167px;height:63px;line-height:63px;font-size:29px}

.site-footer{position:absolute;left:0;top:2294px;width:1200px;height:145px;background:var(--brown)}
.footer-mark{position:absolute;left:76px;top:36px;width:70px;height:70px;border-radius:50%;background:var(--navy)}
.footer-nav{position:absolute;left:174px;top:50px;display:flex;gap:22px;font-size:16px;color:var(--white)}
.copyright{position:absolute;left:174px;top:92px;font-size:13px;color:#f1e4d8}
.copyright b{color:var(--navy)}
.social{position:absolute;left:1068px;top:36px;width:54px;height:54px;border-radius:50%;border:2px solid var(--white)}
</style>
</head>
<body>

<header class="site-header">
  <div class="brand"><span class="brand-mark"></span><span class="brand-name">Harbourlight</span></div>
  <div class="login">
    <svg width="14" height="16" viewBox="0 0 14 16"><rect x="1" y="7" width="12" height="9" rx="1" fill="#8a4b1b"/><path d="M4 7V4.5a3 3 0 0 1 6 0V7" stroke="#8a4b1b" stroke-width="2" fill="none"/></svg>
    Login
  </div>
  <div class="phone">
    <svg width="32" height="32" viewBox="0 0 24 24"><path fill="#8a4b1b" d="M6.6 10.8a15.1 15.1 0 0 0 6.6 6.6l2.2-2.2c.3-.3.7-.4 1-.2 1.1.4 2.3.6 3.6.6.6 0 1 .4 1 1V20c0 .6-.4 1-1 1A17 17 0 0 1 3 4c0-.6.4-1 1-1h3.5c.6 0 1 .4 1 1 0 1.3.2 2.5.6 3.6.1.3 0 .7-.2 1z"/></svg>
    123 456 7890
  </div>
  <div class="search">Search...
    <span class="search-btn"><svg width="18" height="18" viewBox="0 0 18 18"><circle cx="7.5" cy="7.5" r="5" stroke="#fff" stroke-width="2.2" fill="none"/><path d="M11.5 11.5l4.5 4.5" stroke="#fff" stroke-width="2.4"/></svg></span>
  </div>
</header>

<nav class="main-nav">
  <a style="left:80px">Home</a>
  <a style="left:160px">Where to Stay</a>
  <a style="left:335px">Caravan and Camping</a>
  <a style="left:581px">Bed and Breakfast</a>
  <a class="active" style="left:796px">Hotels in Tenby</a>
  <a style="left:1006px">Contact Us</a>
</nav>

<section class="hero" role="img" aria-label="Narrow harbour-town street with pastel houses and hanging flower baskets">
  <h1 class="hero-title display">Harbourlight</h1>
  <p class="hero-text">A popular harbour town visited by over 299,000 visitors a year we hope you enjoy your time visting and breathing in the sea air of Tenby.</p>
  <span class="btn">Contact Us</span>
  <span class="slider-arrow" style="left:8px"><svg width="12" height="16" viewBox="0 0 12 16"><path d="M9 2L3 8l6 6" stroke="#fff" stroke-width="3" fill="none"/></svg></span>
  <span class="slider-arrow" style="left:1150px"><svg width="12" height="16" viewBox="0 0 12 16"><path d="M3 2l6 6-6 6" stroke="#fff" stroke-width="3" fill="none"/></svg></span>
</section>

<h2 class="section-title display"><span class="title-mark"></span><span>Hotels In <span class="accent">Tenby</span></span></h2>
<p class="intro">Most famous for it's Ashcliff Hotel, Tenby actually has over 18 hotels with availability throughout the year. All information for the hotels listed below are valid as of March 2018. To make a booking enquiry, <strong>please contact the hotels directly.</strong></p>

<article class="hotel-card">
  <h3>Ashcliff Hotel</h3>
  <div class="line tel"><svg width="18" height="18" viewBox="0 0 24 24"><path fill="#fff" d="M6.6 10.8a15.1 15.1 0 0 0 6.6 6.6l2.2-2.2c.3-.3.7-.4 1-.2 1.1.4 2.3.6 3.6.6.6 0 1 .4 1 1V20c0 .6-.4 1-1 1A17 17 0 0 1 3 4c0-.6.4-1 1-1h3.5c.6 0 1 .4 1 1 0 1.3.2 2.5.6 3.6.1.3 0 .7-.2 1z"/></svg>01632 960418</div>
  <div class="line small"><svg width="16" height="16" viewBox="0 0 16 16"><circle cx="8" cy="8" r="7" fill="#fff"/></svg>staying@ashcliff-hotel.co.uk</div>
  <div class="line small"><svg width="16" height="16" viewBox="0 0 16 16"><circle cx="8" cy="8" r="7" fill="#fff"/></svg>http://www.ashcliff-hotel.co.uk/</div>
</article>
<div class="photo" style="left:433px;top:896px;width:334px;height:239px;background:linear-gradient(160deg,#dfe6ec,#cfd0c8 60%,#8c8f78)" role="img" aria-label="White hotel entrance with columned porch"></div>
<div class="photo" style="left:789px;top:896px;width:334px;height:239px;background:linear-gradient(180deg,#eef0f2,#c9cbcc 70%,#7c7f80)" role="img" aria-label="Tall white hotel building on a street corner"></div>

<div class="photo" style="left:77px;top:1167px;width:511px;height:298px;background:linear-gradient(180deg,#ddd8cf,#cfc5b4 70%,#6f6a52)" role="img" aria-label="Cream hotel facade with bay windows and balconies"></div>
<div class="photo" style="left:612px;top:1167px;width:511px;height:298px;background:linear-gradient(180deg,#d9c8a2,#cbb48a 65%,#555448)" role="img" aria-label="Yellow hotel front with canopy entrance"></div>

<div class="photo" style="left:77px;top:1496px;width:334px;height:239px;background:linear-gradient(180deg,#3d6f9c,#4f8ab5 50%,#7a8ea0)" role="img" aria-label="Bright blue townhouse hotel under blue sky"></div>
<div class="photo" style="left:433px;top:1496px;width:334px;height:239px;background:linear-gradient(180deg,#3b79b8,#e4bcc4 55%,#c7c7c7)" role="img" aria-label="Modern pink hotel building"></div>
<div class="photo" style="left:789px;top:1496px;width:334px;height:239px;background:linear-gradient(180deg,#d4d7db,#e8e8e6 55%,#3e3f40)" role="img" aria-label="White terrace hotel with balconies"></div>

<div class="photo" style="left:77px;top:1763px;width:511px;height:298px;background:linear-gradient(180deg,#a9b8cf,#8ea3c4 60%,#3a4e6a)" role="img" aria-label="Pale blue inn with iron balcony and hanging flowers"></div>
<div class="photo" style="left:612px;top:1763px;width:511px;height:298px;background:linear-gradient(180deg,#2f5c99,#d8c27c 45%,#c8b470)" role="img" aria-label="Yellow seafront hotel with white window frames"></div>

<p class="tagline">A popular harbour town visited by over 299,000 visitors a year we hope you enjoy your time visting and breathing in the sea air of Tenby.</p>
<span class="btn more">View More</span>

<footer class="site-footer">
  <span class="footer-mark"></span>
  <div class="footer-nav"><span>Home</span><span>Where To Stay</span><span>Caravan And Camping</span><span>Bed And Breakfast</span><span>Hotels In Tenby</span><span>Contact Us</span></div>
  <p class="copyright">©<b>Harbourlight</b> - 2017. All Rights Reserved | Terms and Conditions.</p>
  <span class="social"></span>
</footer>

</body>
</html>
```